Business Card Design Project

Looking to update our business cards. We have a logo with our slogan. We are an IT firm so we wouldlike a modern look.

Industry/Entity Type

Business

```html
<!DOCTYPE html>
<html lang="en">
<head>
<meta charset="utf-8">
<title>Restartly Inc – Business Card</title>
<link href="https://fonts.googleapis.com/css2?family=Jost:wght@400;500&display=swap" rel="stylesheet">
<style>
  :root {
    --lime: #bfc42a;
    --olive: #6a7e2d;
    --olive-deep: #5f7226;
    --paper: #ffffff;
    --ink: #1e1e1e;
    --stage: #e6e6e4;
  }
  * { margin: 0; padding: 0; box-sizing: border-box; }
  html, body { width: 1200px; height: 900px; overflow: hidden; }
  body {
    background: var(--stage);
    font-family: "Jost", "Futura", sans-serif;
    position: relative;
  }
  .card {
    position: absolute;
    top: 297px;
    width: 530px;
    height: 305px;
    border-radius: 18px;
    overflow: hidden;
    background: var(--paper);
    box-shadow: 0 4px 10px rgba(0,0,0,0.25);
  }
  .card--front { left: 50px; }
  .card--back { left: 620px; }
  .card__bg { position: absolute; inset: 0; width: 100%; height: 100%; }

  .wordmark { position: absolute; text-align: center; }
  .wordmark__name {
    display: block;
    font-weight: 500;
    letter-spacing: 7px;
    line-height: 1;
    position: relative;
  }
  .wordmark__inc {
    position: absolute;
    font-size: 9px;
    letter-spacing: 1px;
    top: -8px;
    right: 0;
  }
  .wordmark__tagline {
    display: block;
    font-weight: 500;
    letter-spacing: 2.4px;
    text-transform: uppercase;
  }
  .card--front .wordmark { left: 228px; top: 186px; width: 282px; color: var(--olive); }
  .card--front .wordmark__name { font-size: 36px; }
  .card--front .wordmark__tagline { font-size: 11.5px; margin-top: 10px; }

  .card--back .wordmark { left: 24px; top: 52px; width: 196px; color: var(--paper); text-align: left; }
  .card--back .wordmark__name { font-size: 25px; letter-spacing: 5px; }
  .card--back .wordmark__inc { font-size: 7px; top: -6px; right: 8px; }
  .card--back .wordmark__tagline { font-size: 8px; letter-spacing: 1.8px; margin-top: 6px; }

  .person { position: absolute; left: 45px; top: 222px; }
  .person__name { font-size: 20px; font-weight: 500; color: var(--olive); }
  .person__role { font-size: 12.5px; color: var(--ink); margin-top: 2px; }

  .contact-list { position: absolute; left: 320px; top: 151px; list-style: none; }
  .contact-list li {
    display: flex; align-items: center; gap: 6px;
    font-size: 12.5px; color: var(--ink); line-height: 16px;
  }
  .contact-list svg { width: 10px; height: 10px; fill: var(--olive); flex: none; }
  .address { position: absolute; left: 320px; top: 232px; font-size: 12.5px; line-height: 17px; color: var(--ink); font-style: normal; }
</style>
</head>
<body>

<section class="card card--front" aria-label="Business card front">
  <svg class="card__bg" viewBox="0 0 530 305" preserveAspectRatio="none" aria-hidden="true">
    <rect width="530" height="305" fill="var(--lime)"/>
    <path d="M0,172 C140,110 360,60 530,98 L530,305 L0,305 Z" fill="var(--olive)"/>
    <path d="M0,198 C150,140 370,100 530,150 L530,305 L0,305 Z" fill="var(--paper)"/>
  </svg>
  <div class="wordmark">
    <span class="wordmark__name">RESTARTLY<span class="wordmark__inc">INC</span></span>
    <span class="wordmark__tagline">Making Technology Easy</span>
  </div>
</section>

<section class="card card--back" aria-label="Business card back">
  <svg class="card__bg" viewBox="0 0 530 305" preserveAspectRatio="none" aria-hidden="true">
    <rect width="530" height="305" fill="var(--olive)"/>
    <path d="M0,160 C140,105 360,58 530,78 L530,305 L0,305 Z" fill="var(--lime)"/>
    <path d="M0,204 C150,140 370,100 530,150 L530,305 L0,305 Z" fill="var(--paper)"/>
  </svg>
  <div class="wordmark">
    <span class="wordmark__name">RESTARTLY<span class="wordmark__inc">INC</span></span>
    <span class="wordmark__tagline">Making Technology Easy</span>
  </div>

  <div class="person">
    <p class="person__name">Daniel Morrow</p>
    <p class="person__role">managing director</p>
  </div>

  <ul class="contact-list">
    <li><svg viewBox="0 0 10 10"><path d="M2.5 0h5v10h-5z M3.5 1v6.5h3V1z" fill-rule="evenodd"/></svg>777 412 36 90</li>
    <li><svg viewBox="0 0 10 10"><path d="M2.5 0h5v3h-5z M0 3.5h10v4H8V6H2v1.5H0z M2.5 6.5h5V10h-5z"/></svg>777 412 36 91</li>
    <li><svg viewBox="0 0 10 10"><path d="M0 2h10v6H0z"/><path d="M0 2l5 3.5L10 2" stroke="#fff" stroke-width="0.8" fill="none"/></svg>info@restartly-co.com</li>
    <li><svg viewBox="0 0 10 10"><circle cx="5" cy="5" r="4.6"/><path d="M0.5 5h9M5 0.5v9M2 2.5h6M2 7.5h6" stroke="#fff" stroke-width="0.6" fill="none"/></svg>www.restartly-co.com</li>
  </ul>

  <address class="address">48 Sample Avenue<br>Lakeview, New York 10021</address>
</section>

</body>
</html>
```